Modernization of existing web site

Update existing web site to a professional look vs a home-made site. Site look and navigation should be up to today's standards and display properly on mobile devices.
Only simple HTML and CSS is to be used as this is a basic site. No content management.
Existing site is https://www.plexumar.example

Target Market(s)

Insurance and Technology

Industry/Entity Type

Insurance and technology

Coding

Coded - Design and coding required

Number of Pages Required

5+ page

Font styles to use
Sans Serif

Colors
0054AA
0677BA
7BADD7
CADEEF
E8F1F8
0094D4
00A9DD
6FCCEA
C7EBF8
E9F6FB

Requirements
Must have
• A sleek, modern feel and also done with a button-downed industry in mind.
Nice to have
• Clean integration of the logo and name
Should not have
• Open to ideas

```html
<!DOCTYPE html>
<html lang="en">
<head>
<meta charset="utf-8">
<title>Plexumar — Business and Technology</title>
<link href="https://fonts.googleapis.com/css2?family=Bebas+Neue&family=Open+Sans:wght@400;600&display=swap" rel="stylesheet">
<style>
:root{
  --brand:#2563b8;
  --brand-deep:#1f4fa6;
  --hero-a:#1e4fb0;
  --hero-b:#2a9be0;
  --ink:#222;
  --muted:#555;
  --white:#fff;
  --accent:#f7913d;
  --footer:#444444;
  --footer-deep:#333333;
  --why-a:#2a56ad;
  --why-b:#2f5fbc;
}
*{margin:0;padding:0;box-sizing:border-box}
html,body{width:777px;height:1200px;overflow:hidden;background:var(--white)}
body{position:relative;font-family:"Open Sans",sans-serif;color:var(--ink)}
.abs{position:absolute}
.site-header{position:absolute;left:0;top:0;width:777px;height:66px;background:var(--white)}
.brand{position:absolute;display:flex;align-items:center;gap:5px;font-family:"Open Sans",sans-serif;font-weight:600;font-size:16px;letter-spacing:.3px}
.brand .dot{width:14px;height:14px;border-radius:50%;background:currentColor}
.brand--header{left:49px;top:24px;color:var(--brand)}
.main-nav{position:absolute;top:34px;left:0;width:777px;font-size:7px;color:#444;letter-spacing:.2px}
.main-nav a{position:absolute;color:inherit;text-decoration:none;white-space:nowrap}
.main-nav a.is-active{color:var(--brand)}
.hero{position:absolute;left:0;top:66px;width:777px;height:281px;background:linear-gradient(100deg,var(--hero-a) 0%,#2060c4 40%,var(--hero-b) 100%)}
.hero__art{position:absolute;left:250px;top:0;width:527px;height:281px;background:linear-gradient(160deg,rgba(60,170,235,.55),rgba(20,70,170,.35) 60%,rgba(40,150,230,.6))}
.hero__title{position:absolute;left:76px;top:98px;font-family:"Bebas Neue",sans-serif;font-weight:400;font-size:27px;line-height:29.5px;color:var(--white)}
.intro{position:absolute;left:0;top:392px;width:777px;text-align:center;font-size:10.4px;color:var(--ink)}
.service{position:absolute;top:450px;width:150px;text-align:center}
.service svg{display:block;margin:0 auto;height:36px}
.service h3{font-family:"Bebas Neue",sans-serif;font-weight:400;font-size:13.5px;color:var(--brand-deep);margin-top:13px;letter-spacing:.2px}
.service p{font-size:7.8px;line-height:10px;color:var(--ink);margin-top:8px}
.lead{position:absolute;left:80px;top:603px;width:617px;text-align:center;font-size:10.4px;line-height:19px;color:var(--ink)}
.btn{position:absolute;left:338px;top:680px;width:88px;height:26px;border-radius:5px;background:var(--accent);color:var(--white);font-size:7.5px;display:flex;align-items:center;justify-content:center;text-decoration:none}
.why{position:absolute;left:0;top:778px;width:777px;height:328px}
.why__photo{position:absolute;inset:0;background:linear-gradient(120deg,var(--why-a),var(--why-b) 50%,#3566c0)}
.why__title{position:absolute;left:0;top:36px;width:777px;text-align:center;font-family:"Bebas Neue",sans-serif;font-weight:400;font-size:23px;color:var(--white)}
.reason{position:absolute;color:var(--white)}
.reason__num{position:absolute;left:0;top:0;width:20px;height:20px;border:1px solid rgba(255,255,255,.7);border-radius:50%;font-size:9px;display:flex;align-items:center;justify-content:center}
.reason__rule{position:absolute;left:20px;top:10px;width:55px;height:1px;background:rgba(255,255,255,.7)}
.reason h4{position:absolute;left:87px;top:1px;white-space:nowrap;font-family:"Bebas Neue",sans-serif;font-weight:400;font-size:13.5px}
.reason p{position:absolute;left:88px;top:18px;width:170px;font-size:8.2px;line-height:10px}
.site-footer{position:absolute;left:0;top:1106px;width:777px;height:66px;background:var(--footer)}
.brand--footer{left:49px;top:24px;color:#d8d8d8}
.footer-links a{position:absolute;top:1132px;font-size:8px;color:var(--white);text-decoration:none;white-space:nowrap}
.legal{position:absolute;left:0;top:1172px;width:777px;height:28px;background:var(--footer-deep)}
.legal p{position:absolute;left:598px;top:9px;font-size:8px;color:var(--white)}
</style>
</head>
<body>
<header class="site-header">
  <div class="brand brand--header"><span class="dot"></span>PLEXUMAR</div>
  <nav class="main-nav">
    <a class="is-active" href="#" style="left:387px">HOME</a>
    <a href="#" style="left:446px">OUR SERVICES</a>
    <a href="#" style="left:535px">ABOUT US</a>
    <a href="#" style="left:608px">CONTACT US</a>
    <a href="#" style="left:690px">PRIVACY POLICY</a>
  </nav>
</header>

<section class="hero">
  <div class="hero__art" role="img" aria-label="Isometric illustration of a digital city with a laptop, charts and people working"></div>
  <h1 class="hero__title">Navigating<br>Business and Technology to<br>Generate Results</h1>
</section>

<p class="intro">At PLEXUMAR, we are here to assist you in realizing your vision for your business. We offer a number of different services</p>

<div class="service" style="left:124px">
  <svg viewBox="0 0 40 40" aria-hidden="true"><path d="M2 18 A18 16 0 0 1 38 18 Z" fill="var(--brand-deep)"/><path d="M20 18 V34 a3 3 0 0 1 -6 0" fill="none" stroke="var(--brand-deep)" stroke-width="2"/></svg>
  <h3>Insurance</h3>
  <p>Lorem ipsum dolor sit amet, consectetur adipiscing elit, sed do eiusmod tempor incididunt.</p>
</div>
<div class="service" style="left:303px">
  <svg viewBox="0 0 40 40" aria-hidden="true"><rect x="2" y="2" width="36" height="26" rx="2" fill="none" stroke="var(--brand-deep)" stroke-width="3"/><rect x="17" y="28" width="6" height="6" fill="var(--brand-deep)"/><rect x="11" y="34" width="18" height="3" fill="var(--brand-deep)"/><circle cx="24" cy="13" r="5" fill="none" stroke="var(--brand-deep)" stroke-width="3"/><path d="M7 22 h12 l5 -3" fill="none" stroke="var(--brand-deep)" stroke-width="2.5"/></svg>
  <h3>Technology</h3>
  <p>Lorem ipsum dolor sit amet, consectetur adipiscing elit, sed do eiusmod tempor incididunt.</p>
</div>
<div class="service" style="left:482px">
  <svg viewBox="0 0 40 40" aria-hidden="true"><rect x="2" y="3" width="24" height="34" fill="var(--brand-deep)"/><circle cx="27" cy="22" r="12" fill="var(--brand-deep)" stroke="#fff" stroke-width="2"/><text x="27" y="28" text-anchor="middle" font-family="Open Sans,sans-serif" font-weight="600" font-size="16" fill="#fff">$</text></svg>
  <h3>Financial Services Firm</h3>
  <p>Lorem ipsum dolor sit amet, consectetur adipiscing elit, sed do eiusmod tempor incididunt.</p>
</div>

<p class="lead">We have extensive experience in many areas of business and technology combined with a deep level of integrity in the way we do business. If you have a specific need not mentioned on our website, contact us today with your details.</p>

<a class="btn" href="#">Contact us</a>

<section class="why">
  <div class="why__photo" role="img" aria-label="Blue-tinted photo of a team working at computers in an office"></div>
  <h2 class="why__title">Why Choose Us?</h2>
  <div class="reason" style="left:76px;top:116px"><span class="reason__num">1</span><span class="reason__rule"></span><h4>10+ Years Experience</h4><p>Lorem ipsum dolor sit amet, consectetur adipiscing elit, sed do eiusmod tempor incididunt ut labore et dolore magna aliqua.</p></div>
  <div class="reason" style="left:76px;top:212px"><span class="reason__num">2</span><span class="reason__rule"></span><h4>Dedicated Support 24/7</h4><p>Lorem ipsum dolor sit amet, consectetur adipiscing elit, sed do eiusmod tempor incididunt ut labore et dolore magna aliqua.</p></div>
  <div class="reason" style="left:415px;top:116px"><span class="reason__num">3</span><span class="reason__rule"></span><h4>Agile &amp; Fast Work Style</h4><p>Lorem ipsum dolor sit amet, consectetur adipiscing elit, sed do eiusmod tempor incididunt ut labore et dolore magna aliqua.</p></div>
  <div class="reason" style="left:418px;top:212px"><span class="reason__num">4</span><span class="reason__rule"></span><h4>Safe &amp; Secured</h4><p>Lorem ipsum dolor sit amet, consectetur adipiscing elit, sed do eiusmod tempor incididunt ut labore et dolore magna aliqua.</p></div>
</section>

<footer class="site-footer">
  <div class="brand brand--footer"><span class="dot"></span>PLEXUMAR</div>
</footer>
<nav class="footer-links">
  <a href="#" style="left:477px">Terms of Service</a>
  <a href="#" style="left:558px">Privacy Policy</a>
  <a href="#" style="left:630px">Content Copyright</a>
</nav>
<div class="legal"><p>Copyright © 2022 Plexumar</p></div>
</body>
</html>
```